Halworth Builds, Carpentry Services

Business card for carpentry business in the Sunshine Coast.

Business card layout required using logo provided - provided both PDF copy and AI. Please let me know if you would like a the files for the logo symbol and text by itself.

Business Colours are grey, blue and white. The font colours codes for this design are Blue Hex # 00B4E6 and Hex # 39393B for the gray colour.

FYI font for logo is Gotham Bold.

Preference for a clean and striking layout that is simple and elegant.

Target Market(s)

Young Families, retirees, young couples requiring assistance with small to medium works/renovations on the Sunshine Coast.

Industry/Entity Type

Construction

Contact Information for Business Card

Dean Halworth
Carpenter
0481356027
dean@halworthbuilds.com.au
Brightwater Bay, Palm Coast
RHLA Licensed Carpenter (In smaller font)

Font styles to use
Sans Serif

Colors

Designer to choose colors to be used in the design.

Requirements
Must have
• Logo provided must appear on the card, preferably on one side of the card by itself with the text on the alternate side
Nice to have
• Text on the other side of card, maybe grey background and white font here but happy for the designer to provide ideas here.
Should not have
• Use of other colours, other than the ones provided - white, grey and blue. Black optional.

```html
<!DOCTYPE html>
<html lang="en">
<head>
<meta charset="utf-8">
<title>Halworth Builds – Business Card</title>
<link rel="stylesheet" href="https://fonts.googleapis.com/css2?family=Montserrat:wght@400;500;700&display=swap">
<style>
  :root {
    --page: #d9d9db;
    --card: #39393b;
    --card-deep: #303032;
    --blue: #00b4e6;
    --blue-soft: #4fa8dc;
    --white: #ffffff;
    --silver: #d6d6d8;
    --rule: #7a7a7e;
  }
  * { box-sizing: border-box; margin: 0; padding: 0; }
  html, body {
    width: 1200px; height: 985px; overflow: hidden;
    background: var(--page);
    font-family: "Montserrat", sans-serif;
  }
  .card {
    position: absolute;
    left: 232px;
    width: 736px; height: 420px;
    background: linear-gradient(160deg, var(--card) 0%, var(--card-deep) 100%);
    border-bottom: 6px solid var(--blue-soft);
    box-shadow: 0 10px 24px rgba(0,0,0,.28);
    color: var(--white);
  }
  .card--front { top: 55px; }
  .card--back { top: 510px; }

  .brand {
    display: flex; align-items: center; gap: 14px;
    font-weight: 700; letter-spacing: 2px; text-transform: uppercase;
    white-space: nowrap;
  }
  .brand__mark { width: 22px; height: 22px; flex: none; }
  .card--front .brand {
    position: absolute; left: 0; right: 0; top: 0; bottom: 0;
    justify-content: center;
    font-size: 40px; color: var(--silver);
  }
  .card--front .brand__mark { background: var(--silver); }
  .card--back .brand {
    position: absolute; right: 52px; top: 70px;
    font-size: 28px; color: var(--blue-soft);
  }
  .card--back .brand__mark { background: var(--blue-soft); width: 18px; height: 18px; }

  .contact {
    position: absolute; left: 60px; top: 178px;
  }
  .contact__name {
    font-weight: 700; font-size: 30px; color: var(--blue-soft);
    text-transform: uppercase; letter-spacing: .5px; white-space: nowrap;
  }
  .contact__role { font-size: 16px; margin-top: 2px; }
  .contact__list { list-style: none; margin-top: 26px; }
  .contact__item {
    display: flex; align-items: center; gap: 12px;
    font-size: 17px; margin-bottom: 10px; letter-spacing: .5px; white-space: nowrap;
  }
  .contact__icon { width: 15px; height: 15px; flex: none; }

  .divider {
    position: absolute; left: 160px; right: 52px; top: 254px;
    height: 1px; background: var(--rule);
  }
  .licence {
    position: absolute; right: 52px; bottom: 40px;
    font-size: 15px; letter-spacing: .8px;
  }
</style>
</head>
<body>

<section class="card card--front">
  <div class="brand"><span class="brand__mark"></span>Halworth Builds</div>
</section>

<section class="card card--back">
  <div class="brand"><span class="brand__mark"></span>Halworth Builds</div>

  <div class="contact">
    <h1 class="contact__name">Dean Halworth</h1>
    <p class="contact__role">Carpenter</p>
    <ul class="contact__list">
      <li class="contact__item">
        <svg class="contact__icon" viewBox="0 0 24 24" fill="none" stroke="var(--blue-soft)" stroke-width="2.2"><path d="M5 3h4l2 5-2.5 1.5a11 11 0 0 0 6 6L16 13l5 2v4a2 2 0 0 1-2 2A17 17 0 0 1 3 5a2 2 0 0 1 2-2z"/></svg>
        0481356027
      </li>
      <li class="contact__item">
        <svg class="contact__icon" viewBox="0 0 24 24"><rect x="2" y="5" width="20" height="14" fill="var(--blue-soft)"/><path d="M2 5l10 8 10-8" fill="none" stroke="var(--card)" stroke-width="2"/></svg>
        dean@halworthbuilds.com.au
      </li>
      <li class="contact__item">
        <svg class="contact__icon" viewBox="0 0 24 24" fill="none" stroke="var(--blue-soft)" stroke-width="2"><path d="M12 22s7-7 7-12a7 7 0 0 0-14 0c0 5 7 12 7 12z"/><circle cx="12" cy="10" r="2.5"/></svg>
        Brightwater Bay, Palm Coast
      </li>
    </ul>
  </div>

  <div class="divider"></div>
  <p class="licence">RHLA Licensed Carpenter</p>
</section>

</body>
</html>
```